Stock Broking Firm - Web Design Project

We are looking at doing a full re-design of our home page and content page and moving the majority of our content over to DNN.

Phase 1 : Website redesign www.kalvernequities.com.au

The current design is too washed out, boring and has no call to action buttons.

Solution:

KL Equities is looking for a brighter/ cleaner redesign with a few stand out call to action buttons.

• Banner with logo across the top horizontally - Bright blue logo on white background similar to www.dmq.com.au - CALL 1300 482 917 - Follow on Chirper / Facespace
• Horizontal menu bar - professional looking. - Home - About Us- Our Services - Membership - Open an Account - Become a member - Contact
• Below banner top left - large rotating banner - maybe zimbo gallery style www.tvhaldrens.com.au
• Right of rotating banner - Membership login
• Below members login - Register for Daily Market Report/ research blog - Large bright button / Name / Email / Phone / pop up??
• Below Register for daily market report - Market Indicies - RSS feed of delayed data from QNW see www.tvhaldrens.com
• Below Market indicies - KL EQUITIES - Market Tweets ( feed from our chirper page)

Below Rotating Banner -

content area

Below content area - 4 large block buttons see www.crandwickley.com.au ( hover over change colour)

Button 1 - EDUCATION - content - click here for more

Button 2 - Market Information and Research

Button 3 - Full service Broker - content brief - click here for more

Button 4 - Trade Commodities and Options

below buttons - small horizontal menu bar slightly different colour incl - Careers/ Partners / Legal Privacy FSG Site Map

Regards,
Colin Marsh

Target Market(s)

35 - 65

Industry/Entity Type

Education

Requirements
Must have
• Follow brief above - large banner, call to action buttons, F.S. Chirper, Member login etc. 4 big buttons
Nice to have
• clean looking site similar to www.dmq.com.au / not too busy. Corporate looking.
Should not have
• not too busy

```html
<!DOCTYPE html>
<html lang="en">
<head>
<meta charset="utf-8">
<title>KL Equities</title>
<link rel="stylesheet" href="https://fonts.googleapis.com/css2?family=Roboto+Condensed:wght@400&family=Source+Sans+3:wght@400;600&display=swap">
<style>
:root{
  --teal:#0b5b7b;
  --teal-dark:#084a66;
  --title:#1c5c7c;
  --link:#1f3fa8;
  --text:#4a4a4a;
  --ink:#1e1e1e;
  --line:#d6d6d6;
  --card:#f2f2f2;
  --sky:#35c8f4;
}
*{box-sizing:border-box;margin:0;padding:0}
html,body{width:1076px;height:1200px;overflow:hidden;background:#fff}
body{position:relative;font-family:"Source Sans 3",sans-serif;color:var(--text);font-size:10px}
.abs{position:absolute}
.topline{left:0;top:0;width:1076px;height:3px;background:#555}
.brand{left:140px;top:14px}
.brand-name{font-family:"Source Sans 3",sans-serif;font-size:40px;font-weight:400;color:var(--teal);line-height:1;display:flex;align-items:center;gap:8px}
.brand-name .mark{width:26px;height:26px;background:var(--teal)}
.brand-tag{margin-left:48px;margin-top:6px;font-size:9px;color:#555;line-height:11px;text-align:right;width:220px}
.search{left:816px;top:33px;width:116px;height:29px;border:1px solid #ddd;font-size:10px;color:#2a5d7a;padding:8px 9px}
.search svg{position:absolute;right:7px;top:7px}
.nav{left:0;top:91px;width:1076px;height:27px;background:var(--teal)}
.nav a{position:absolute;top:0;line-height:27px;color:#fff;font-size:10.5px;text-decoration:none;transform:translateX(-50%)}
.nav i{position:absolute;top:0;width:1px;height:27px;background:#3a7f9b}
.nav-shadow{left:170px;top:118px;width:735px;height:6px;background:radial-gradient(ellipse at top,rgba(0,0,0,.35),rgba(0,0,0,0) 70%)}
.slider{left:142px;top:132px;width:568px;height:286px;background:radial-gradient(ellipse at 55% 60%,#2f7cff,#0b3fb0 45%,#031545 100%)}
.slider-shadow{left:142px;top:417px;width:568px;height:10px;background:radial-gradient(ellipse at top,rgba(0,0,0,.6),rgba(0,0,0,0) 70%)}
.arrow{top:258px}
.box{border:1px solid var(--line);background:#fff}
.box h3{font-family:"Roboto Condensed",sans-serif;font-weight:400;font-size:14px;color:var(--title)}
.field{height:24px;border:1px solid #ddd;font-size:9px;color:#555;padding:6px 8px;margin-top:6px}
.btn{background:var(--teal);color:#fff;font-size:10.5px;padding:3px 9px;float:right;margin-top:8px}
.login{left:716px;top:132px;width:221px;height:125px;padding:11px 10px}
.register{left:716px;top:265px;width:221px;height:154px;padding:11px 10px}
.card{top:440px;width:191px;height:168px;background:var(--card);border:1px solid #e2e2e2;padding:10px 12px;box-shadow:0 1px 2px rgba(0,0,0,.08)}
.card h4{font-family:"Roboto Condensed",sans-serif;font-weight:400;font-size:14.5px;color:var(--title);border-bottom:1px solid #ccc;padding-bottom:5px}
.card p{margin-top:12px;font-size:10px;line-height:18.2px;text-align:justify;color:#555}
.card a{display:block;margin-top:13px;color:var(--link);font-size:10px;text-decoration:underline}
.panel{border:1px solid var(--line);background:#fff}
.bar{background:var(--teal);color:#fff;font-family:"Roboto Condensed",sans-serif;font-size:14.5px;height:24px;line-height:24px;padding-left:7px}
.news{left:142px;top:626px;width:584px;height:210px;padding:4px}
.item{position:relative;padding:9px 8px 4px 42px;border-bottom:1px solid #ccc;margin:0 4px;font-size:10px;line-height:15.7px}
.item:last-child{border:0}
.item b{font-weight:400;color:var(--ink);display:block}
.item span{color:var(--link)}
.item svg{position:absolute;left:8px;top:11px}
.indices{left:736px;top:626px;width:203px;height:210px;padding:5px 4px}
table{border-collapse:collapse;width:100%;font-size:9px;color:#222}
th{font-weight:400;color:var(--title);font-size:10px;height:21px;border-right:1px solid #ddd;background:#f3f3f3}
td{height:21.5px;padding-left:7px;border-right:1px solid #ddd}
th:last-child,td:last-child{border-right:0}
tr:nth-child(odd) td{background:#f2f2f2}
.services{left:142px;top:843px;width:584px;height:210px;padding:4px}
.svc{margin:0 4px;padding:10px 10px 6px;border-bottom:1px solid #ccc;font-size:10px;line-height:12.5px;color:var(--ink)}
.svc:last-child{border:0}
.svc h5{font-family:"Roboto Condensed",sans-serif;font-weight:400;font-size:13px;color:#1e3fa8;margin-bottom:1px}
.social{left:736px;top:843px;width:203px;height:210px;padding:8px}
.social .follow{font-size:13px;font-weight:600;color:var(--sky);line-height:14px}
.feed{position:absolute;left:9px;top:42px;width:185px;height:159px;background:var(--sky);padding:14px 6px 0}
.tw{position:relative;padding:0 4px 12px 20px;font-size:9px;line-height:13.2px;color:#113;border-bottom:1px solid #1f9ec8;margin-bottom:12px}
.tw:last-child{border:0}
.tw em{font-style:normal;color:#fff;display:block}
.tw::before{content:"";position:absolute;left:7px;top:3px;border-left:4px solid #113;border-top:3px solid transparent;border-bottom:3px solid transparent}
.footer{left:0;top:1062px;width:1076px;height:138px;background:linear-gradient(#eee,#fff 25%,#fff 80%,#ececec)}
.footer-links{left:0;width:1076px;text-align:center;top:1112px;font-size:9.5px;color:#222;line-height:18px}
.bottomline{left:0;top:1197px;width:1076px;height:3px;background:#555}
</style>
</head>
<body>
<div class="abs topline"></div>

<div class="abs brand">
  <div class="brand-name"><span class="mark"></span>KL Equities</div>
  <div class="brand-tag">shares | options | commodities | foreign exchange<br>ABN 47 203 815 226 | licence no 528 904</div>
</div>

<div class="abs search">Search
  <svg width="14" height="15" viewBox="0 0 14 15"><circle cx="5.5" cy="5.5" r="4" fill="none" stroke="#2a5d7a" stroke-width="2"/><path d="M8.5 8.5l4 5" stroke="#2a5d7a" stroke-width="2.5"/></svg>
</div>

<nav class="abs nav">
  <a style="left:189px">Home</a><i style="left:247px"></i>
  <a style="left:300px">About Us</a><i style="left:357px"></i>
  <a style="left:413px">Our Services</a><i style="left:471px"></i>
  <a style="left:527px">Membership</a><i style="left:584px"></i>
  <a style="left:643px">Open an Account</a><i style="left:699px"></i>
  <a style="left:757px">Become a member</a><i style="left:811px"></i>
  <a style="left:876px">Contact</a>
</nav>
<div class="abs nav-shadow"></div>

<div class="abs slider" role="img" aria-label="Rotating banner: blue stock ticker board with market figures"></div>
<div class="abs slider-shadow"></div>
<svg class="abs arrow" style="left:160px" width="16" height="26" viewBox="0 0 16 26"><path d="M13 2L3 13l10 11" fill="none" stroke="#fff" stroke-width="3.5"/></svg>
<svg class="abs arrow" style="left:672px" width="16" height="26" viewBox="0 0 16 26"><path d="M3 2l10 11-10 11" fill="none" stroke="#fff" stroke-width="3.5"/></svg>

<section class="abs box login">
  <h3>MEMBERS LOGIN</h3>
  <div class="field" style="margin-top:8px">username</div>
  <div class="field">Profile</div>
  <span class="btn">Login</span>
</section>

<section class="abs box register">
  <h3>REGISTER</h3>
  <div class="field" style="margin-top:8px">Name</div>
  <div class="field">E mail</div>
  <div class="field">Phone</div>
  <span class="btn">Register</span>
</section>

<article class="abs card" style="left:142px"><h4>Education</h4><p>Lorem Ipsum is simply dummy text of the printing and typesetting industry. Lorem Ipsum has been the industry's standard dummy tex</p><a>Click Here Learn More</a></article>
<article class="abs card" style="left:343px"><h4>Market Information and Research</h4><p>Lorem Ipsum is simply dummy text of the printing and typesetting industry. Lorem Ipsum has been the industry's standard dummy tex</p><a>Click Here Learn More</a></article>
<article class="abs card" style="left:545px"><h4>Full service Broker</h4><p>Lorem Ipsum is simply dummy text of the printing and typesetting industry. Lorem Ipsum has been the industry's standard dummy tex</p><a>Click Here Learn More</a></article>
<article class="abs card" style="left:747px"><h4>Trade Commodities and Options</h4><p>Lorem Ipsum is simply dummy text of the printing and typesetting industry. Lorem Ipsum has been the industry's standard dummy tex</p><a>Click Here Learn More</a></article>

<section class="abs panel news">
  <div class="bar">Latest News</div>
  <div class="item">
    <svg width="15" height="17" viewBox="0 0 15 17"><rect x=".5" y=".5" width="14" height="16" fill="#f4f4f4" stroke="#aaa"/><path d="M3 5h9M3 8h9M3 11h9" stroke="#999"/></svg>
    <b>Skyline Travel boycotted Meridian Airways</b><span>Skyline Travel staff were told to stop selling Meridian Airways flights after the carrier refused a request to engage in price fixing, a court has heard.</span>
  </div>
  <div class="item">
    <svg width="15" height="17" viewBox="0 0 15 17"><rect x=".5" y=".5" width="14" height="16" fill="#f4f4f4" stroke="#aaa"/><path d="M3 5h9M3 8h9M3 11h9" stroke="#999"/></svg>
    <b>BKN challenges Nexora, Orchard</b><span>Better apps and a strong history of banking are the keys to beating global tech giants like Orchard and Nexora, according to BKN Australia chief executive Dean Halloway</span>
  </div>
  <div class="item">
    <svg width="15" height="17" viewBox="0 0 15 17"><rect x=".5" y=".5" width="14" height="16" fill="#f4f4f4" stroke="#aaa"/><path d="M3 5h9M3 8h9M3 11h9" stroke="#999"/></svg>
    <b>Torrant Aussie bond book tops $2 billion</b><span>Updated | Mining giant Torrant Minerals has now attracted over $2 billion of orders from investors for its first Australian bond offering in more than a decade. The order book is now closed and the transaction will be priced later today.</span>
  </div>
</section>

<section class="abs panel indices">
  <div class="bar">Market Inidicaes</div>
  <table>
    <thead><tr><th>Name</th><th>Value</th><th>+/-</th><th>%+/-</th></tr></thead>
    <tbody>
      <tr><td>All Shrs</td><td>4,501.96</td><td>-11.84</td><td>-11.84</td></tr>
      <tr><td>KSX200</td><td>4,481.86</td><td>-12.54</td><td>-12.54</td></tr>
      <tr><td>Dalt</td><td>13,578.39</td><td>-31.76</td><td>-31.76</td></tr>
      <tr><td>Hanlo</td><td>20,824.56</td><td>-187.82</td><td>-187.82</td></tr>
      <tr><td>NORVEX</td><td>3,111.38</td><td>-24.81</td><td>-24.81</td></tr>
      <tr><td>Kaito</td><td>8,863.30</td><td>-</td><td>-</td></tr>
      <tr><td>R&amp;T500</td><td>1,460.93</td><td>-</td><td>-</td></tr>
    </tbody>
  </table>
</section>

<section class="abs panel services">
  <div class="bar" style="padding-left:12px">Our Services</div>
  <div class="svc"><h5>BROKERAGE</h5>Whether you want a trade only or full service, find out about our competitive brokerage fees, we are confident you will be impressed. more...</div>
  <div class="svc"><h5>RESEARCH</h5>Our comprehensive QR7 Report &amp; Daily updates includes detailed global market summaries, sector analysis and recommen-dations for the long term investor through to the agressive trader. more...</div>
  <div class="svc"><h5>KL MEMBERSHIP</h5>Our Value for money membership gives you everything you need in one handy place. Further information is available on our Members page. more...</div>
</section>

<section class="abs panel social">
  <div class="follow">Follow us on Chirper</div>
  <div class="feed">
    <div class="tw">Lorem Ipsum is simply dummy text of the printing and typeset-ting industry<em>1 Hour Ago</em></div>
    <div class="tw">Lorem Ipsum is simply dummy text of the printing and typeset-ting industry<em>1 Hour Ago</em></div>
  </div>
</section>

<footer class="abs footer"></footer>
<div class="abs footer-links">Careers &nbsp; / &nbsp; Partners &nbsp; / &nbsp; Legal Privacy FSG Site Map<br>Copyrights @2012 All Rights Reserved</div>
<div class="abs bottomline"></div>
</body>
</html>
```